PRP Poster

We need a poster for a doctors room to encourage people to enquire about PRP procedure.

It needs to include "for osteoarthritis and sports injuries" and "enhancing the body's natural ability to heal".

A brochure is attached which outlines what PRP (Platelet Rich Plasma) is, in the brochure it is called DVX. DO NOT USE ANY OF THE LOGOS FROM THIS BROCHURE.

Target Market(s)

patients in an orthopaedic surgery waiting room/area
age range from teenagers till 80year olds
male= female ratio

Requirements
Must have
• single poster
eye-catching yet professional
needs to be suitable/appropriate for the waiting area of a surgeons clinic
Nice to have
• prp is a natural therapy (it is essentially the person's own blood being reinjected to a site of injury)
the "natural" aspect of the therapy needs to be emphasised

```html
<!DOCTYPE html>
<html lang="en">
<head>
<meta charset="utf-8">
<title>PRP Poster</title>
<link rel="stylesheet" href="https://fonts.googleapis.com/css2?family=Oswald:wght@500;700&family=Roboto+Condensed:wght@400;700&display=swap">
<style>
  :root {
    --page: #e9ecee;
    --paper: #ffffff;
    --blood-dark: #6e0a0d;
    --blood: #b0161b;
    --blood-light: #e0383a;
    --title-blue: #1a6fc0;
    --band-blue: #1767b8;
    --navy: #1e3a6b;
    --navy-deep: #15294f;
    --natural-yellow: #ffe21a;
    --badge-red: #e01f26;
    --white: #ffffff;
    --frame: #cfd3d6;
  }
  * { margin: 0; padding: 0; box-sizing: border-box; }
  html, body {
    width: 1200px; height: 798px; overflow: hidden;
    background: var(--page);
  }
  .canvas {
    width: 1200px; height: 798px;
    display: flex; align-items: center; justify-content: center;
  }
  .poster {
    width: 520px; height: 746px;
    background: var(--paper);
    border: 6px solid var(--frame);
    display: flex; flex-direction: column;
    overflow: hidden;
    font-family: "Roboto Condensed", sans-serif;
  }
  .poster-hero {
    height: 300px;
    display: flex; align-items: center; justify-content: center;
  }
  .hero-word {
    font-family: "Oswald", sans-serif;
    font-weight: 700;
    font-size: 300px;
    line-height: 1;
    letter-spacing: -6px;
    background: radial-gradient(circle at 30% 35%, var(--blood-light), var(--blood) 45%, var(--blood-dark) 100%);
    -webkit-background-clip: text;
    background-clip: text;
    color: transparent;
    transform: scaleY(1.05);
  }
  .poster-title {
    font-family: "Oswald", sans-serif;
    font-weight: 500;
    color: var(--title-blue);
    font-size: 49px;
    line-height: 1;
    text-align: center;
    padding: 4px 0 10px;
  }
  .claim-band {
    background: var(--band-blue);
    color: var(--white);
    text-align: center;
    padding: 8px 10px 10px;
  }
  .claim-headline {
    font-family: "Oswald", sans-serif;
    font-weight: 500;
    font-size: 33px;
    line-height: 1.1;
  }
  .claim-headline .natural { color: var(--natural-yellow); font-weight: 700; }
  .claim-note {
    font-size: 15px;
    font-weight: 700;
    margin-top: 4px;
  }
  .poster-lower {
    flex: 1;
    background: linear-gradient(180deg, var(--navy) 0%, var(--navy-deep) 100%);
    position: relative;
  }
  .indication-badge {
    position: absolute; left: 14px; top: 22px;
    width: 92px; height: 92px; border-radius: 50%;
    background: var(--badge-red);
    color: var(--white);
    display: flex; align-items: center; justify-content: center;
    text-align: center;
    font-weight: 700; font-size: 15px; line-height: 1.05;
    padding: 8px;
    transform: rotate(-14deg);
  }
  .anatomy-visual {
    position: absolute; left: 96px; top: 14px;
    width: 200px; height: 236px;
  }
  .healing-claim {
    position: absolute; right: 18px; top: 50px;
    width: 200px;
    color: var(--white);
    font-family: "Roboto Condensed", sans-serif;
    font-weight: 700;
    font-size: 36px;
    line-height: 1.05;
  }
  .healing-claim .natural { color: var(--natural-yellow); }
</style>
</head>
<body>
<main class="canvas">
  <article class="poster">
    <header class="poster-hero">
      <h1 class="hero-word">PRP</h1>
    </header>
    <h2 class="poster-title">Platelet Rich Plasma</h2>
    <section class="claim-band">
      <p class="claim-headline">A new method of <span class="natural">NATURAL</span> therapy</p>
      <p class="claim-note">It is essentially the person's own blood being reinjected to a site of injury</p>
    </section>
    <section class="poster-lower">
      <p class="indication-badge">for osteoarthritis and sports injuries</p>
      <svg class="anatomy-visual" viewBox="0 0 200 236" role="img" aria-label="Collage of glowing medical scans of joints and the human body">
        <defs>
          <radialGradient id="scanGlow" cx="50%" cy="45%" r="60%">
            <stop offset="0%" stop-color="#5aa3e6"/>
            <stop offset="55%" stop-color="#2c5d9c"/>
            <stop offset="100%" stop-color="#1e3a6b" stop-opacity="0"/>
          </radialGradient>
        </defs>
        <rect width="200" height="236" fill="url(#scanGlow)"/>
      </svg>
      <p class="healing-claim">enhancing the body's <span class="natural">natural</span> ability to heal</p>
    </section>
  </article>
</main>
</body>
</html>
```